New Internet Service provider for regional or isolated businesses

I'm looking for a logo and basic information website for an Internet company - "Quill Harbor Internet". This new company will be providing specialised Internet connectivity for isolated areas or where connectivity is too expensive for one business.
i.e Bringing Businesses together for better more affordable Internet.
3 Types of Pages
1. Home Page
2. Content Page templates
3. More Information Form
1. Contact Name. 2. Business Address. 3. Business Phone Number. 4. Mobile Phone. 5. Number of Staff 6. Current Internet connection . 7. Speed 8. Comments ?
Web Pages
**Quill Harbor Internet **
Bringing Businesses together for better Internet
Who is Quill Harbor Internet ?
How do we work ?
Which carriers ?
Technologies Used ?
Contact details
Check my address now ?
(Form)
Our company will be using Fibre and Microwave/Radio technology to connect remote businesses to high speed Internet
Target Market(s)
Business customers with minimum 10 staff outside metropolitan areas
Industry/Entity Type
Internet Service Provider
Coding
Coded - Design and coding required
Number of Pages Required
3 page
Requirements
Must have
- 3 Types of Pages
- 1. Home Page
- 2. Content Page templates (See above)
- 3. "More Information" Form
- 1. Contact Name. 2. Business Address. 3. Business Phone Number. 4. Mobile Phone. 5. Number of Staff 6.Current Internet connection . 7. Speed 8.Comments ?
Nice to have
- Pictures of fibre optics, radio towers, stock photos of businesses / PC's
- Some ideas on the companies we will be using (I am looking for something similar in my website).
- In order of preference
- 1. www.pelmara.com.au
- 2. www.drusket.com,au
- 3.www.tolvent.com.au

```html
<!DOCTYPE html>
<html lang="en">
<head>
<meta charset="utf-8">
<title>Quill Harbor Internet</title>
<link href="https://fonts.googleapis.com/css2?family=Montserrat:wght@300;400;500;600;700;800&display=swap" rel="stylesheet">
<style>
:root{
  --blue:#2f6fc7;
  --blue-dark:#1f57a8;
  --blue-light:#4a90e2;
  --ink:#1b1b1b;
  --body:#555;
  --line:#d9dde3;
  --white:#fff;
}
*{margin:0;padding:0;box-sizing:border-box}
html,body{width:1200px;height:3125px;overflow:hidden}
body{font-family:'Montserrat',sans-serif;color:var(--body);background:var(--white);position:relative}

/* header */
.site-header{position:absolute;left:0;top:0;width:1200px;height:120px;background:var(--white);z-index:3}
.brand{position:absolute;left:100px;top:0;height:120px;display:flex;align-items:center;gap:10px}
.brand-dot{width:26px;height:26px;border-radius:50%;background:var(--blue);flex:none}
.brand-name{font-size:17px;font-weight:700;color:var(--blue);letter-spacing:.3px;white-space:nowrap}
.main-nav{position:absolute;top:0;left:400px;display:flex;height:120px}
.main-nav a{display:block;font-size:14px;font-weight:600;color:var(--ink);text-decoration:none;
  letter-spacing:.5px;padding:56px 26px 0;height:120px;position:relative}
.main-nav a.active{color:var(--blue)}
.main-nav a.active::after{content:"";position:absolute;left:0;right:0;bottom:0;height:4px;background:var(--blue)}

/* hero */
.hero{position:absolute;left:0;top:120px;width:1200px;height:610px;
  background:linear-gradient(180deg,#7fb2de 0%,#b9d5ea 38%,#6f9e3c 52%,#3f7a1e 100%)}
.hero h1{position:absolute;left:100px;top:148px;color:var(--white);font-weight:800;font-size:54px;line-height:57px;letter-spacing:.5px}
.hero-arrow{position:absolute;top:250px;width:46px;height:46px;border-radius:50%;background:rgba(0,0,0,.25);display:flex;align-items:center;justify-content:center}
.hero-curve{position:absolute;left:0;top:680px;z-index:2}

/* welcome */
.section-title{position:absolute;left:0;width:1200px;text-align:center;font-weight:700;font-size:34px;color:var(--ink);letter-spacing:.5px}
.section-title em{font-style:normal;color:var(--blue)}
.lead{position:absolute;left:200px;width:800px;text-align:center;font-size:14px;font-weight:400;line-height:27px;color:var(--body)}
.divider{position:absolute;left:215px;top:907px;width:770px;height:1px;background:var(--line)}
.feature{position:absolute;top:943px;width:320px;text-align:center}
.feature-icon{width:148px;height:148px;margin:0 auto;border-radius:50%;border:5px solid #e7eef8;
  background:radial-gradient(circle at 50% 35%,var(--blue-light),var(--blue-dark));display:flex;align-items:center;justify-content:center}
.feature h3{margin-top:22px;font-size:19px;font-weight:700;color:var(--ink);letter-spacing:.5px}
.feature p{margin-top:12px;font-size:13px;line-height:24px;color:var(--body)}
.btn-outline{display:inline-block;margin-top:26px;width:154px;height:44px;line-height:42px;border:2px solid var(--blue);color:var(--blue);font-size:14px;font-weight:500;text-decoration:none}

/* carriers band */
.carriers{position:absolute;left:0;top:1335px;width:1200px;height:534px;
  background:linear-gradient(100deg,#2a3648 0%,#5b6d88 35%,#8c7a6c 50%,#3b5b8e 70%,#2b4a7e 100%)}
.carriers::after{content:"";position:absolute;inset:0;background:rgba(20,40,80,.35)}
.carriers h2,.carriers p,.carriers .btn-solid{position:absolute;z-index:1}
.carriers h2{left:0;width:1200px;top:146px;text-align:center;color:var(--white);font-size:34px;font-weight:700;letter-spacing:.5px}
.carriers p{left:160px;width:880px;top:204px;text-align:center;color:#eef2f8;font-size:14px;line-height:28px}
.btn-solid{left:485px;top:290px;width:230px;height:54px;line-height:50px;text-align:center;background:var(--blue);border:2px solid #6ea3e8;color:var(--white);font-size:19px;font-weight:600;text-decoration:none}

/* specialised */
.service-card{position:absolute;top:2040px;width:310px;height:253px;border:1px solid var(--line);background:var(--white)}
.service-card .photo{position:absolute;left:14px;top:12px;width:282px;height:192px}
.service-card h4{position:absolute;left:0;width:100%;top:216px;text-align:center;font-size:19px;font-weight:400;color:var(--ink)}

/* form */
.info-form{position:absolute;left:0;top:2360px;width:1200px;height:442px;
  background:linear-gradient(135deg,#3a78cc 0%,#4f8fe0 45%,#2f69bd 100%)}
.info-form h2{position:absolute;left:0;width:1200px;top:48px;text-align:center;color:var(--white);font-size:30px;font-weight:700;letter-spacing:.5px}
.field{position:absolute;width:318px;height:36px;background:var(--white);border:1px solid #c9d6e8;font-size:12px;color:#8a8f98;padding:10px 14px}
.field.comments{height:136px}
.submit{position:absolute;left:98px;top:350px;width:183px;height:44px;background:var(--blue-dark);border:2px solid #8cb8ee;color:var(--white);font-size:16px;font-weight:600;text-align:center;line-height:40px;letter-spacing:.5px}

/* footer */
.site-footer{position:absolute;left:0;top:2802px;width:1200px;height:323px;background:linear-gradient(180deg,#4a92e6,#3b80d6)}
.foot-col{position:absolute;top:42px;color:var(--white)}
.foot-col h5{font-size:16px;font-weight:600;letter-spacing:.5px;margin-bottom:16px}
.foot-col li{list-style:none;font-size:13px;line-height:30px;color:#eaf2fc}
.foot-col.bordered{border-right:1px solid rgba(255,255,255,.3);height:190px}
.contact-line{display:flex;align-items:flex-start;gap:12px}
.contact-line svg{margin-top:9px;flex:none}
.social{display:flex;gap:6px;margin-top:18px}
.social-link{width:36px;height:36px;border-radius:50%;border:2px solid var(--white);background:var(--blue-dark);display:flex;align-items:center;justify-content:center}
.foot-rule{position:absolute;left:100px;top:252px;width:1000px;height:1px;background:rgba(255,255,255,.35)}
.copyright{position:absolute;left:100px;top:276px;font-size:12px;color:#eaf2fc}
</style>
</head>
<body>

<header class="site-header">
  <div class="brand"><span class="brand-dot"></span><span class="brand-name">QUILL HARBOR INTERNET</span></div>
  <nav class="main-nav">
    <a class="active">HOME</a>
    <a>COMPANY</a>
    <a>CARRIER PARTNERS AND TECHNOLOGIES</a>
    <a>CONTACT US</a>
  </nav>
</header>

<section class="hero" role="img" aria-label="Photo of a businesswoman cheering with a laptop in an office chair on a green field under blue sky">
  <h1>BRINGING<br>BUSINESSES<br>TOGETHER<br>FOR BETTER<br>INTERNET</h1>
  <div class="hero-arrow" style="left:20px"><svg width="16" height="16" viewBox="0 0 16 16"><path d="M11 2 5 8l6 6" fill="none" stroke="#fff" stroke-width="2"/></svg></div>
  <div class="hero-arrow" style="right:20px"><svg width="16" height="16" viewBox="0 0 16 16"><path d="M5 2l6 6-6 6" fill="none" stroke="#fff" stroke-width="2"/></svg></div>
</section>
<svg class="hero-curve" width="1200" height="60" viewBox="0 0 1200 60"><path d="M0 48 Q600 -20 1200 48 L1200 60 L0 60Z" fill="#fff"/></svg>

<h2 class="section-title" style="top:742px">WELCOME TO <em>QUILL HARBOR INTERNET</em></h2>
<p class="lead" style="top:800px">Sed ut perspiciatis unde omnis iste natus error sit voluptatem accusantium doloremque laudantium, totam rem aperiam, eaque ipsa quae ab illo inventore veritatis et quasi architecto beatae vitae dicta sunt explicabo. Nemo enim ipsam voluptatem quia voluptas sit aspernatur aut odit aut fugit.</p>
<div class="divider"></div>

<div class="feature" style="left:84px">
  <div class="feature-icon"><svg width="70" height="70" viewBox="0 0 70 70" fill="none" stroke="#fff" stroke-width="5" stroke-linecap="round"><circle cx="35" cy="38" r="22"/><path d="M35 26v13l8 6M12 16l9-7M58 16l-9-7M20 60l-4 5M50 60l4 5"/></svg></div>
  <h3>SAVES TIME!</h3>
  <p>Our company will be providing specialised<br>Internet connectivity for isolated areas or<br>where connectivity is too expensive.</p>
  <a class="btn-outline">READ MORE</a>
</div>
<div class="feature" style="left:440px">
  <div class="feature-icon"><svg width="74" height="70" viewBox="0 0 74 70" fill="none" stroke="#fff" stroke-width="5" stroke-linecap="round" stroke-linejoin="round"><circle cx="40" cy="20" r="14"/><path d="M6 58l12-12h14l10 4h16M6 40h14l10 6"/></svg></div>
  <h3>SAVES MONEY!</h3>
  <p>Our company will be providing specialised<br>Internet connectivity for isolated areas or<br>where connectivity is too expensive.</p>
  <a class="btn-outline">READ MORE</a>
</div>
<div class="feature" style="left:796px">
  <div class="feature-icon"><svg width="70" height="70" viewBox="0 0 70 70" fill="none" stroke="#fff" stroke-width="6" stroke-linecap="round" stroke-linejoin="round"><path d="M26 14l9-8 9 8M16 34 8 50h18M54 34l8 16H44"/><path d="M35 6 22 28M48 30l10 18M26 58h18"/></svg></div>
  <h3>HIGH SPEED!</h3>
  <p>Our company will be providing specialised<br>Internet connectivity for isolated areas or<br>where connectivity is too expensive.</p>
  <a class="btn-outline">READ MORE</a>
</div>

<section class="carriers" role="img" aria-label="Photo of two businessmen shaking hands in front of glass office towers">
  <h2>CARRIER PARTNERS AND TECHNOLOGIES</h2>
  <p>Sed ut perspiciatis unde omnis iste natus error sit voluptatem accusantium doloremque laudantium, totam rem aperiam, eaque ipsa quae ab illo inventore veritatis et quasi architecto beatae vitae dicta sunt explicabo.</p>
  <a class="btn-solid">READ MORE »</a>
</section>

<h2 class="section-title" style="top:1910px">OUR COMPANY <em>SPECIALISED</em></h2>
<p class="lead" style="top:1960px">Our company will be providing specialised Internet connectivity for isolated areas or where connectivity is too expensive for one business</p>

<div class="service-card" style="left:98px">
  <div class="photo" role="img" aria-label="Illustration of a city skyline with a glowing globe and satellite for fibre technology" style="background:linear-gradient(180deg,#1b3f8a,#3f7fd0 60%,#a9c8ea)"></div>
  <h4>FIBRE TECHNOLOGY</h4>
</div>
<div class="service-card" style="left:444px">
  <div class="photo" role="img" aria-label="Photo of a support agent wearing a headset in an office" style="background:linear-gradient(135deg,#d8cbbd,#c49a7a 50%,#7d6a5c)"></div>
  <h4>MICROWAVE TECHNOLOGY</h4>
</div>
<div class="service-card" style="left:790px">
  <div class="photo" role="img" aria-label="Photo of a businessman on the phone with a tablet at a desk with a computer" style="background:linear-gradient(135deg,#d9dde2,#8a6a5a 50%,#5a3a3a)"></div>
  <h4>REMOTE BUSINESSES</h4>
</div>

<section class="info-form">
  <h2>MORE INFORMATION</h2>
  <div class="field" style="left:98px;top:121px">Contact Name</div>
  <div class="field" style="left:441px;top:121px">Business Address</div>
  <div class="field" style="left:784px;top:121px">Business Phone Number</div>
  <div class="field" style="left:98px;top:190px">Mobile Phone</div>
  <div class="field" style="left:441px;top:190px">Number of Staff</div>
  <div class="field" style="left:784px;top:190px">Current Internet connection</div>
  <div class="field" style="left:98px;top:259px">Speed</div>
  <div class="field comments" style="left:441px;top:259px;width:661px">Comments ?</div>
  <div class="submit">SUBMIT NOW</div>
</section>

<footer class="site-footer">
  <div class="foot-col bordered" style="left:100px;width:150px">
    <h5>COMPANY</h5>
    <ul><li>Home</li><li>Company</li><li>Carrier Partners</li><li>Technologies</li><li>Contact Us</li></ul>
  </div>
  <div class="foot-col bordered" style="left:275px;width:190px">
    <h5>SERVICES</h5>
    <ul><li>Save Time</li><li>Save Money</li><li>High Speed</li><li>Others</li></ul>
  </div>
  <div class="foot-col bordered" style="left:498px;width:240px">
    <h5>GET IN TOUCH</h5>
    <ul>
      <li class="contact-line"><svg width="12" height="12" viewBox="0 0 12 12"><path d="M2 1h3l1 3-2 1a7 7 0 0 0 3 3l1-2 3 1v3c-6 1-10-3-9-9z" fill="#fff"/></svg>Call us on (07) 5550 1842</li>
      <li class="contact-line"><svg width="13" height="10" viewBox="0 0 13 10"><rect width="13" height="10" fill="#fff"/><path d="M0 0l6.5 5L13 0" fill="none" stroke="#3f86dc"/></svg>hello@quillharbor.net</li>
      <li class="contact-line"><svg width="10" height="14" viewBox="0 0 10 14"><path d="M5 0a5 5 0 0 1 5 5c0 4-5 9-5 9S0 9 0 5a5 5 0 0 1 5-5z" fill="#fff"/><circle cx="5" cy="5" r="2" fill="#3f86dc"/></svg><span>Quill Harbor Internet<br>Level 9, 48 Tarrow Lane<br>Calder Bay Qld 4870</span></li>
    </ul>
  </div>
  <div class="foot-col bordered" style="left:769px;width:130px">
    <h5>WHY US</h5>
    <ul><li>Customers</li><li>Team</li><li>FAQ</li><li>Contact</li></ul>
  </div>
  <div class="foot-col" style="left:925px;width:200px">
    <h5>FOLLLOW US</h5>
    <ul><li>Please connect with us on</li></ul>
    <div class="social" aria-label="Social network links">
      <span class="social-link"><svg width="14" height="14" viewBox="0 0 14 14"><path d="M3 11 11 3M5 3h6v6" fill="none" stroke="#fff" stroke-width="2"/></svg></span>
      <span class="social-link"><svg width="14" height="14" viewBox="0 0 14 14"><path d="M3 11 11 3M5 3h6v6" fill="none" stroke="#fff" stroke-width="2"/></svg></span>
      <span class="social-link"><svg width="14" height="14" viewBox="0 0 14 14"><path d="M3 11 11 3M5 3h6v6" fill="none" stroke="#fff" stroke-width="2"/></svg></span>
      <span class="social-link"><svg width="14" height="14" viewBox="0 0 14 14"><path d="M3 11 11 3M5 3h6v6" fill="none" stroke="#fff" stroke-width="2"/></svg></span>
    </div>
  </div>
  <div class="foot-rule"></div>
  <p class="copyright">© 2016 Quill Harbor Internet&nbsp; All right reserved&nbsp; Term of Use</p>
</footer>

</body>
</html>
```